Web Design Project

To develop a web based Council Meeting Support system which includes 2 major components for each Council member:
1. Allow a council member to Vote on a motion during a council session
2. Allow a council member to flag notify the Chair their intention to speak on a motion
The application will have 3 separate interfaces:
Chair interface: Allows the Chair of the session to review voting and manage the speaker queue
Council interface: Allows each council member to vote on each motion and add flag their intention to speak for or against a motion
Admin interface: Allows administrators to initiate a session and import details on all meeting participants
We will begin by designing the Council Interface. (An example wireframe is attached) This council interface will give members the ability to request to speak, vote, view voting results and viewing the current motion number.
*** 4 Designs will be required overall. One for each interface and a login page ***
Needs to be designed so that it works well on an Velbo or any tablet device.
Update: Looking for a brighter design, not a dark grey one. The blue colour from trm.on.ca would be good.
Flag
- Request to Speak
Voting
Vote Results
Current Motion Number

```html
<!DOCTYPE html>
<html lang="en">
<head>
<meta charset="utf-8">
<title>Council Interface – Motion 12</title>
<link rel="stylesheet" href="https://fonts.googleapis.com/css2?family=Arimo:wght@400;700&display=swap">
<style>
:root{
  --page-light:#f4f8fc;
  --page-soft:#dfe9f4;
  --panel-fill:#ffffff;
  --panel-frame:#b9cde3;
  --brand-blue:#0b5cad;
  --brand-blue-deep:#07427f;
  --bar-strip:#8fb6de;
  --blue:#0a4fb0;
  --blue-glow:#4aa6f0;
  --green:#068a14;
  --green-glow:#3fe04a;
  --orange:#b85a06;
  --orange-glow:#f0a012;
  --white:#ffffff;
  --ink:#14283f;
  --name-text:#23374f;
}
*{margin:0;padding:0;box-sizing:border-box}
html,body{width:1200px;height:949px;overflow:hidden}
body{
  font-family:"Arimo",Arial,sans-serif;
  color:var(--white);
  background:radial-gradient(ellipse 75% 65% at 55% 30%,var(--page-light),var(--page-soft) 85%);
  position:relative;
}
.brand{position:absolute;left:110px;top:40px;display:flex;align-items:center;gap:14px;color:var(--brand-blue-deep)}
.brand-mark{width:30px;height:30px;background:var(--brand-blue-deep)}
.brand-name{font-weight:700;font-size:22px;line-height:1.15}
.motion-bar{
  position:absolute;left:625px;top:19px;width:575px;height:85px;
  background:linear-gradient(90deg,var(--brand-blue-deep) 0%,var(--brand-blue) 55%,#6fa3d8 100%);
}
.motion-label{position:absolute;left:681px;top:50px;font-weight:700;font-size:21px}
.motion-number{
  position:absolute;left:968px;top:9px;width:161px;height:104px;
  background:radial-gradient(ellipse at 50% 15%,var(--orange-glow),var(--orange) 75%);
  font-weight:700;font-size:70px;display:flex;align-items:center;justify-content:center;
}
.panel{
  position:absolute;background:var(--panel-fill);
  border:8px solid var(--panel-frame);
}
.panel-speak{left:55px;top:134px;width:1079px;height:327px}
.panel-vote{left:55px;top:477px;width:429px;height:432px}
.section-head{
  position:absolute;background:var(--brand-blue);
  border-bottom:12px solid var(--bar-strip);
  font-weight:700;font-size:21px;display:flex;align-items:center;justify-content:center;
}
.head-speak{left:69px;top:172px;width:385px;height:86px}
.head-vote{left:69px;top:515px;width:403px;height:88px}
.head-results{left:530px;top:515px;width:604px;height:88px;background:var(--brand-blue-deep)}
.btn{
  position:absolute;width:314px;height:69px;font-weight:700;font-size:28px;
  display:flex;align-items:center;justify-content:center;
}
.btn-blue{background:radial-gradient(ellipse 55% 80% at 50% 25%,var(--blue-glow),var(--blue) 80%)}
.btn-green{background:radial-gradient(ellipse 55% 80% at 50% 25%,var(--green-glow),var(--green) 80%)}
.btn-orange{background:radial-gradient(ellipse 55% 80% at 50% 25%,var(--orange-glow),var(--orange) 80%)}
.col-head{
  position:absolute;top:618px;width:166px;height:48px;background:var(--brand-blue);
  font-weight:700;font-size:28px;display:flex;align-items:center;justify-content:center;
}
.name-list{position:absolute;top:688px;list-style:none;font-size:19px;line-height:25.3px;color:var(--name-text)}
</style>
</head>
<body>
  <div class="brand"><span class="brand-mark"></span><span class="brand-name">Trillium Registry<br>Members</span></div>

  <div class="motion-bar"></div>
  <div class="motion-label">CURRENT MOTION:</div>
  <div class="motion-number">12</div>

  <section class="panel panel-speak"></section>
  <div class="section-head head-speak">I WOULD LIKE TO SPEAK:</div>
  <div class="btn btn-blue" style="left:712px;top:174px">FOR MOTION</div>
  <div class="btn btn-blue" style="left:712px;top:258px">AGAINST MOTION</div>
  <div class="btn btn-green" style="left:712px;top:344px">REMOVE</div>

  <section class="panel panel-vote"></section>
  <div class="section-head head-vote">VOTING:</div>
  <div class="btn btn-blue" style="left:111px;top:621px">FOR</div>
  <div class="btn btn-blue" style="left:111px;top:707px">AGAINST</div>
  <div class="btn btn-orange" style="left:111px;top:792px">ABSTAIN</div>

  <div class="section-head head-results">VOTE RESULTS:</div>
  <div class="col-head" style="left:548px">FOR</div>
  <div class="col-head" style="left:749px">AGAINST</div>
  <div class="col-head" style="left:950px">ABSTAIN</div>

  <ul class="name-list" style="left:577px"><li>A. Dorval</li><li>S. Maren</li><li>P. Hollister</li><li>L Varma</li><li>T. Okoro</li><li>R.A. Linden</li><li>S.K. Rao</li><li>S. Maren</li><li>L. Quill</li></ul>
  <ul class="name-list" style="left:778px"><li>A. Dorval</li><li>S. Maren</li><li>P. Hollister</li><li>L Varma</li><li>T. Okoro</li><li>R.A. Linden</li><li>S.K. Rao</li><li>S. Maren</li><li>L. Quill</li></ul>
  <ul class="name-list" style="left:979px"><li>A. Dorval</li><li>S. Maren</li><li>P. Hollister</li><li>L Varma</li><li>T. Okoro</li><li>R.A. Linden</li><li>S.K. Rao</li><li>S. Maren</li><li>L. Quill</li></ul>
</body>
</html>
```